Fernvale Pte Ltd

I want a creative and stand out web page so when my client search for my web page or google search. The front page is stand out and they know that we are the interior office designer that are searching for . We are commercial office design company. We also have the video to put at our front page for client to see. Natural is the key elements. As we like to carry recycle materials , plant , trees is our key element such as biophilic design
Updates

Hi All,

For my web page, I need minimalist design and creative frontpage.
When my client search for my web page, they straight feel that this is the office design company.
The webpage is special and nature is the key element for the design.
My company logo can be design in the shaped of the letter OO in the webpage.
Below is the sample you can refer.

https://www.pinboardly.example/pin/592716408361528037/

Target Market(s)

Customer searching for office design

Industry/Entity Type

Commerical designer firm- Office interior design & Build company

Number of Pages Required

5+ page

Font styles to use
Other font styles liked:
• Wilmina

Colors
59FF00
82FF00
B8FF75
E3FFCB
F4FFEA
FFC000
F8CF3A
FAE287
FDF2CF
FEFAEE
6B429C
8869AF
B7A5CE
E3DAEB
F3F0F8

Requirements
Must have
• Home, Services,Gallery, Calculator, Testimonials, Contact, Blog
Nice to have
• Natural, creative, minimalist
Should not have
• No black color or blue color

```html
<!DOCTYPE html>
<html lang="en">
<head>
<meta charset="utf-8">
<title>Fernvale Pte Ltd — Commercial Interior Design &amp; Office Renovation</title>
<link href="https://fonts.googleapis.com/css2?family=Roboto:wght@300;400;500;700&family=Roboto+Condensed:wght@400;700&display=swap" rel="stylesheet">
<style>
:root{
  --purple:#6B429C;
  --purple-soft:#8869AF;
  --lilac:#E3DAEB;
  --yellow:#FFC000;
  --lime:#59FF00;
  --ink:#333333;
  --text:#555555;
  --grey-bg:#EEEEEE;
  --dark-btn:#2F2F2F;
  --footer:#333333;
  --white:#FFFFFF;
}
*{box-sizing:border-box;margin:0;padding:0}
html,body{width:1200px;height:4167px;overflow:hidden;background:var(--white)}
body{position:relative;font-family:'Roboto',Arial,sans-serif;color:var(--text)}
a{text-decoration:none}
.abs{position:absolute}
.photo{position:absolute}
.btn{position:absolute;display:flex;align-items:center;justify-content:center;gap:6px;background:var(--dark-btn);color:var(--white);font-family:'Roboto',Arial,sans-serif;font-weight:500;font-size:15px;text-transform:uppercase;text-decoration:none}
.btn .chev{width:13px;height:13px}

/* nav */
.topline{top:0;left:0;width:1200px;height:3px;background:var(--lilac)}
.nav{top:31px;left:570px;display:flex;font-size:14px;color:#444;letter-spacing:.3px}
.nav a{color:#444;margin-right:21px}

/* hero */
.hero-panel{top:80px;left:0;width:551px;height:584px;background:var(--purple)}
.hero-photo{top:80px;left:551px;width:649px;height:584px;background:linear-gradient(180deg,#f4f1ea 0%,#e8e2d8 35%,#6e3a2a 50%,#7a4632 62%,#5c5a5c 80%,#4a484a 100%)}
.hero-title{top:230px;left:38px;color:var(--white);font-weight:400;font-size:41px;line-height:42px;letter-spacing:-.5px}
.hero-lead{top:323px;left:38px;width:460px;color:var(--white);font-weight:300;font-size:18px;line-height:28px}
.hero-btn{top:437px;left:38px;width:191px;height:52px;border-radius:26px;background:var(--lilac);color:var(--purple);font-size:13px;display:flex;align-items:center;justify-content:center}
.play{top:316px;left:839px;width:84px;height:84px}

/* welcome */
.wel-a{top:720px;left:0;width:230px;height:248px;background:linear-gradient(160deg,#efe9e1,#6b4a36 60%,#3b3130)}
.wel-b{top:980px;left:0;width:230px;height:252px;background:linear-gradient(180deg,#cfd8d0,#8dae5a 55%,#5b7a2e)}
.wel-c{top:720px;left:243px;width:346px;height:512px;background:linear-gradient(180deg,#ddd8d2 0%,#c9c1b6 50%,#b48a4e 80%,#3d3a3a 100%)}
.eyebrow{top:736px;left:655px;color:var(--yellow);font-family:'Roboto Condensed',Arial,sans-serif;font-size:22px;letter-spacing:.5px}
.brand-title{top:758px;left:653px;color:var(--purple);font-family:'Roboto Condensed',Arial,sans-serif;font-weight:700;font-size:43px;line-height:52px}
.brand-sub{top:810px;left:658px;width:380px;color:#444;font-size:18px;line-height:27px}
.wel-text{top:873px;left:658px;width:372px;font-size:15px;line-height:24px}
.wel-btn{top:1143px;left:661px;width:158px;height:53px}

/* calculators */
.calc-band{top:1296px;left:0;width:1200px;height:418px;background:var(--grey-bg)}
.card{position:absolute;top:1361px;width:205px;height:285px;background:var(--white);text-align:center;padding-top:28px}
.card svg{width:92px;height:92px}
.card h3{font-weight:500;font-size:16px;color:#444;line-height:22px;margin:10px 14px 6px}
.card p{font-size:11.5px;line-height:18px;color:#666;margin:0 16px}
.calc-title{top:1362px;left:832px;color:var(--purple);font-family:'Roboto Condensed',Arial,sans-serif;font-weight:700;font-size:24px}
.calc-text{top:1398px;left:835px;width:210px;font-size:13px;line-height:19.5px}
.calc-btn{top:1596px;left:838px;width:136px;height:46px}

/* gallery */
.gal-title{top:1762px;left:0;width:1200px;text-align:center;color:var(--purple);font-family:'Roboto Condensed',Arial,sans-serif;font-weight:700;font-size:43px}
.gal-sub{top:1817px;left:0;width:1200px;text-align:center;font-size:17px;color:#555}
.g1{top:1875px;left:160px;width:285px;height:230px;background:linear-gradient(180deg,#e6e4de,#b9b2a7 55%,#c59a5e)}
.g2{top:1875px;left:457px;width:285px;height:230px;background:linear-gradient(180deg,#d5d0c8,#bdb4a6 55%,#b68646)}
.g3{top:1875px;left:753px;width:284px;height:230px;background:linear-gradient(180deg,#ece8e2,#6b4b36 55%,#cfc4b3)}
.g4{top:2118px;left:160px;width:285px;height:230px;background:linear-gradient(180deg,#3d3533,#c9b595 60%,#d9c6a2)}
.g5{top:2118px;left:457px;width:580px;height:230px;background:linear-gradient(180deg,#e7e3dd,#bdb6ab 55%,#4b4747)}
.gal-btn{top:2382px;left:522px;width:168px;height:53px}

/* services */
.svc-band{top:2494px;left:0;width:1200px;height:633px;background:var(--grey-bg)}
.svc-title{top:2538px;left:0;width:1200px;text-align:center;color:#333;font-weight:500;font-size:30px;line-height:38px}
.svc-text{top:2627px;left:195px;width:810px;text-align:center;font-size:12.5px;line-height:19px}
.s1{top:2714px;left:0;width:355px;height:322px;background:linear-gradient(160deg,#f0efed,#cfcac5 50%,#8a7c70)}
.s2{top:2714px;left:374px;width:450px;height:322px;background:linear-gradient(180deg,#9a5a46,#b23a3a 35%,#4a4242 65%,#a88a64)}
.s3{top:2714px;left:843px;width:357px;height:322px;background:linear-gradient(160deg,#f3f3f1,#d9d9d6 60%,#b6b6b3)}
.svc-label{position:absolute;top:3055px;font-size:17px;color:#444}

/* green design */
.green-title{top:3183px;left:160px;color:var(--purple);font-family:'Roboto Condensed',Arial,sans-serif;font-weight:700;font-size:43px;line-height:43px}
.green-text{top:3293px;left:160px;width:390px;font-size:15.5px;line-height:24px}
.green-btn{top:3636px;left:161px;width:168px;height:54px}
.r1{top:3190px;left:608px;width:347px;height:512px;background:linear-gradient(180deg,#e6e1da,#7a5a3e 45%,#3e3a3a 75%,#6b4a32)}
.r2{top:3190px;left:968px;width:232px;height:205px;background:linear-gradient(180deg,#4f7a34,#6c9a40 55%,#3b3b3b)}
.r3{top:3410px;left:968px;width:232px;height:292px;background:linear-gradient(180deg,#7c5b3e,#e5e2de 50%,#3c3a3a)}

/* footer */
.footer{top:3803px;left:0;width:1200px;height:302px;background:var(--footer)}
.brand-name{top:3862px;left:176px;color:var(--white);font-weight:400;font-size:24px;line-height:30px}
.badge{top:3905px;left:320px;width:62px;height:24px;background:#777;border-radius:3px}
.foot-about{top:3942px;left:160px;width:250px;color:#ddd;font-size:11px;line-height:19px}
.foot-h{position:absolute;top:3867px;color:var(--white);font-weight:500;font-size:12.5px;text-transform:uppercase}
.foot-list{position:absolute;list-style:none;color:#ddd;font-size:9.5px;text-transform:uppercase;line-height:27px}
.news-text{top:3897px;left:836px;width:210px;color:#ddd;font-size:10.5px;line-height:17px}
.news-input{top:3962px;left:838px;width:200px;height:35px;border:1px solid #bbb;color:#ddd;font-size:10.5px;padding:11px 10px}
.news-btn{top:4011px;left:838px;width:114px;height:35px;background:var(--lilac);color:#333;font-size:13px;font-weight:500;display:flex;align-items:center;justify-content:center}
.bottom-bar{top:4105px;left:0;width:1200px;height:62px;background:var(--lime)}
.copy{top:4128px;left:164px;font-size:11.5px;color:#333}
.social{top:4122px;left:898px;display:flex;gap:9px}
.social span{width:29px;height:29px;border:2px solid #333;border-radius:50%}
</style>
</head>
<body>

<div class="abs topline"></div>
<nav class="abs nav">
  <a href="#">HOME</a><a href="#">SERVICES</a><a href="#">GALLERY</a><a href="#">CALCULATOR</a><a href="#">TESTIMONIALS</a><a href="#">CONTACT</a><a href="#">BLOG</a>
</nav>

<section>
  <div class="abs hero-panel"></div>
  <h1 class="abs hero-title">YOUR SPACE,<br>YOUR SIGNATURE STYLE</h1>
  <p class="abs hero-lead">Ultimately, interior design aims to create enviroments that enhance the quality of life, evoke certain moods or emotions.</p>
  <a class="abs hero-btn" href="#">BOOK APPOINTMENT</a>
  <div class="photo hero-photo" role="img" aria-label="Video still of a boardroom with wood-panelled walls, white conference table and black office chairs"></div>
  <svg class="abs play" viewBox="0 0 84 84" aria-label="Play video">
    <circle cx="42" cy="42" r="39" fill="none" stroke="#fff" stroke-width="3"/>
    <path d="M34 27 L58 42 L34 57 Z" fill="none" stroke="#fff" stroke-width="3" stroke-linejoin="round"/>
  </svg>
</section>

<section>
  <div class="photo wel-a" role="img" aria-label="Office pantry with wood cabinetry and bar seating"></div>
  <div class="photo wel-b" role="img" aria-label="Green planted lounge corner by a window"></div>
  <div class="photo wel-c" role="img" aria-label="Timber staircase with seating and plants"></div>
  <p class="abs eyebrow">WELCOME TO</p>
  <h2 class="abs brand-title">FERNVALE SINGAPORE</h2>
  <p class="abs brand-sub">A Singapore Reputable Commercial Interior Design &amp; Office Renovation Company</p>
  <p class="abs wel-text">No matter what type of commercial space you have, whether it is an office, corporate firm, restaurant, spa, salon, plaza, mall, or any retail shop, we are here to provide the highest level of interior design and renovation services to match your needs. Our creative ideas and innovative solutions to commercial renovation projects can transform any workspace or building into a masterpiece. Let our professional and experienced team of designers turn your dreams into reality – one step at a time.</p>
  <a class="btn wel-btn" href="#">READ MORE <svg class="chev" viewBox="0 0 14 14"><circle cx="7" cy="7" r="7" fill="#fff"/><path d="M5.5 3.8 L8.8 7 L5.5 10.2" fill="none" stroke="#2F2F2F" stroke-width="2"/></svg></a>
</section>

<section>
  <div class="abs calc-band"></div>
  <div class="card" style="left:160px">
    <svg viewBox="0 0 92 92"><circle cx="46" cy="46" r="46" fill="#FFC000"/><g fill="none" stroke="#333" stroke-width="2.5"><rect x="30" y="24" width="32" height="44"/><rect x="36" y="31" width="6" height="6"/><rect x="50" y="31" width="6" height="6"/><rect x="36" y="43" width="6" height="6"/><rect x="50" y="43" width="6" height="6"/><rect x="42" y="56" width="8" height="12"/></g></svg>
    <h3>Office Floor Space Calculator</h3>
    <p>Unsure how much office space do you need for renovation? Use our office space calculator here.</p>
  </div>
  <div class="card" style="left:377px">
    <svg viewBox="0 0 92 92"><circle cx="46" cy="46" r="46" fill="#FFC000"/><g fill="none" stroke="#333" stroke-width="2.5"><path d="M28 64 Q24 40 40 36 Q56 40 52 64 Z"/><path d="M34 30 L46 30 L42 36 L38 36 Z"/><rect x="50" y="42" width="16" height="22"/><line x1="53" y1="48" x2="63" y2="48"/></g><text x="40" y="58" font-size="14" font-family="Roboto,sans-serif" fill="#333" text-anchor="middle">$</text></svg>
    <h3>Renovation Budget Calculator</h3>
    <p>How much should you budget for office renovation? Try out our renovation budget calculator here.</p>
  </div>
  <div class="card" style="left:593px">
    <svg viewBox="0 0 92 92"><circle cx="46" cy="46" r="46" fill="#FFC000"/><g fill="none" stroke="#333" stroke-width="2.5"><circle cx="46" cy="46" r="24"/><path d="M46 30 L46 46 L56 52"/></g></svg>
    <h3>Project Timeline Calculator</h3>
    <p>In order to know your office renovation and relocation timescale. Use this project timeline calculator.</p>
  </div>
  <h2 class="abs calc-title">OUR CALCULATORS</h2>
  <p class="abs calc-text">Lorem Ipsum is simply dummy typesetting industry. Lorem Ipsum has been the industry's standard dummy text ever since the 1500s, when an unknown printer took a galley of type and scrambled it to centuries, but also the leap into electronic typesetting, remaining essentially unchanged.</p>
  <a class="btn calc-btn" href="#">CONTACT US</a>
</section>

<section>
  <h2 class="abs gal-title">PROJECT GALLERY</h2>
  <p class="abs gal-sub">Explore our work. Let our design portfolio speaks for itself.</p>
  <div class="photo g1" role="img" aria-label="Open café area with round tables and city windows"></div>
  <div class="photo g2" role="img" aria-label="Timber stair seating with lounge chairs"></div>
  <div class="photo g3" role="img" aria-label="Pantry bar with stools and warm lighting"></div>
  <div class="photo g4" role="img" aria-label="Manager office with light oak desk and dark cabinets"></div>
  <div class="photo g5" role="img" aria-label="Long white boardroom table with mesh chairs"></div>
  <a class="btn gal-btn" href="#">VIEW MORE <svg class="chev" viewBox="0 0 14 14"><circle cx="7" cy="7" r="7" fill="#fff"/><path d="M5.5 3.8 L8.8 7 L5.5 10.2" fill="none" stroke="#2F2F2F" stroke-width="2"/></svg></a>
</section>

<section>
  <div class="abs svc-band"></div>
  <h2 class="abs svc-title">Your One-Stop Office Renovation<br>&amp; Interior Design Partner</h2>
  <p class="abs svc-text">Designing a new office or remolding an existing one involves a tedious process. Fernvale wants to make it easier for you. We will guide you from start to end of the journey. To ensure that the project will be well organised and communicated, a dedicated project manager will be assigned. Discover our various services that can turn your creative ideas into reality.</p>
  <div class="photo s1" role="img" aria-label="Designer sketching a floor layout at a desk"></div>
  <div class="photo s2" role="img" aria-label="Renovated open office with red partitions and workstations"></div>
  <div class="photo s3" role="img" aria-label="Hand drawing a space plan on paper"></div>
  <span class="svc-label" style="left:66px">Office Space Partitioning</span>
  <span class="svc-label" style="left:519px">Office Renovation</span>
  <span class="svc-label" style="left:948px">Office Space Planning</span>
</section>

<section>
  <h2 class="abs green-title">THE GREEN DESIGN<br>REVOLUTION</h2>
  <p class="abs green-text">With our commitment to support eco-friendly solutions, we specialise in 'green design". Our interior design solutions contribute positively to the overall health of the inhabitants of a specific area while considering various environmental factors. We ensure that a sustainable solution will be catered to you. Our green design is balance with aesthetics, functionality, and design quality. Most of the resources used are environment friendly. Our building and construction practices are also eco-friendly. We see it as our responsibility to help preserve and nurture the Earth. It is this environmental consciousness that appeals most to our prospective clientele.</p>
  <a class="btn green-btn" href="#">READ MORE <svg class="chev" viewBox="0 0 14 14"><circle cx="7" cy="7" r="7" fill="#fff"/><path d="M5.5 3.8 L8.8 7 L5.5 10.2" fill="none" stroke="#2F2F2F" stroke-width="2"/></svg></a>
  <div class="photo r1" role="img" aria-label="Private office with walnut panels and ergonomic chair"></div>
  <div class="photo r2" role="img" aria-label="Meeting room with a living green wall"></div>
  <div class="photo r3" role="img" aria-label="White meeting table beside timber wall"></div>
</section>

<footer>
  <div class="abs footer"></div>
  <p class="abs brand-name">Fernvale Pte Ltd</p>
  <div class="abs badge" aria-label="Certification badge"></div>
  <p class="abs foot-about">since the 1500s, when an unknown printer took ing and typesetting industry. Lorem Ipsum has been the industry's standard dummy text ever since the 1500s, when an unknown printer took a specimen book. It has survived only five text</p>

  <h4 class="foot-h" style="left:454px">Calculator Tools</h4>
  <ul class="foot-list" style="top:3908px;left:454px">
    <li>Office Space Calculator</li><li>Renovation Budget Calculator</li><li>Project Timeline Calculator</li>
  </ul>

  <h4 class="foot-h" style="left:661px">Our Services</h4>
  <ul class="foot-list" style="top:3905px;left:661px">
    <li>Services Overview</li><li>Office Interior Design</li><li>Office Space Planning</li><li>Office Partitioning</li><li>Office Renovation</li>
  </ul>

  <h4 class="foot-h" style="left:836px">Signup for Newsletter</h4>
  <p class="abs news-text">Be rewarded with exclusive member offers, including discounts, sales, freebies, gifts-with purchase and competitions.</p>
  <div class="abs news-input">your email</div>
  <div class="abs news-btn">SUBSCRIBE</div>

  <div class="abs bottom-bar"></div>
  <p class="abs copy">© 2023 fernvale.example. All Rights Reserved</p>
  <div class="abs social" aria-label="Social links"><span></span><span></span><span></span><span></span></div>
</footer>

</body>
</html>
```